Chateau de Vormelle Investment Brochure

I need a brochure that can be used both online and as printed version to direct people to which explains the investment opportunity at Chateau de Vormelle. We are offering shares in the chateau, its operating company and 4 weeks 5 star accommodation per annum in a suite of the investors choice. The design should appeal to people looking at holiday homes but also be serious enough to attract investors.

Target Market(s)

Affluent 35+ seeking investment opportunity

Industry/Entity Type

Investment

```html
<!DOCTYPE html>
<html lang="en">
<head>
<meta charset="utf-8">
<title>Chateau de Vormelle – Investment Opportunities</title>
<link href="https://fonts.googleapis.com/css2?family=Libre+Baskerville:wght@400;700&family=Rokkitt:wght@700&display=swap" rel="stylesheet">
<style>
  :root {
    --paper: #ffffff;
    --ink: #1b1b1b;
    --navy: #253f8f;
    --sky: #87a5d6;
    --lime: #c2d92f;
    --photo-light: #e9e6e1;
    --photo-warm: #b98a5c;
  }
  html, body {
    margin: 0;
    padding: 0;
    overflow: hidden;
    background: var(--paper);
  }
  .brochure-page {
    position: relative;
    width: 927px;
    height: 1200px;
    overflow: hidden;
    background: var(--paper);
    color: var(--ink);
    font-family: "Libre Baskerville", Georgia, serif;
  }
  .header-band {
    position: absolute;
    left: 0;
    top: 128px;
    width: 927px;
    height: 118px;
    background: linear-gradient(180deg,
      rgba(37, 63, 143, 0.55) 0%,
      rgba(135, 165, 214, 0.45) 50%,
      rgba(194, 217, 47, 0.35) 85%,
      rgba(194, 217, 47, 0) 100%);
  }
  .brand-name {
    position: absolute;
    top: 92px;
    right: 75px;
    margin: 0;
    font-family: "Libre Baskerville", Georgia, serif;
    font-weight: 400;
    font-size: 15px;
    color: var(--ink);
    white-space: nowrap;
  }
  .suite-photo {
    position: absolute;
    left: 111px;
    top: 267px;
    width: 333px;
    height: 249px;
    border: 2px solid var(--lime);
    border-radius: 22px;
    background: linear-gradient(180deg, var(--photo-light) 0%, #dcd8d2 62%, var(--photo-warm) 100%);
  }
  .offer {
    position: absolute;
    left: 111px;
    top: 549px;
    width: 780px;
  }
  .offer-title {
    margin: 0 0 9px;
    font-family: "Rokkitt", "Rockwell", serif;
    font-weight: 700;
    font-size: 21px;
    letter-spacing: 0.4px;
    text-transform: uppercase;
    color: var(--lime);
    line-height: 24px;
  }
  .offer p {
    margin: 0 0 25.7px;
    font-size: 16.8px;
    line-height: 25.7px;
  }
  .offer .indent {
    display: block;
    padding-left: 54px;
  }
</style>
</head>
<body>
<main class="brochure-page">
  <div class="header-band" role="img" aria-label="Decorative header band in navy, light blue and lime"></div>

  <p class="brand-name">Chateau de Vormelle</p>

  <div class="suite-photo" role="img" aria-label="Photo of a bright suite lounge with a round table, cane chairs, leather armchairs and a television"></div>

  <section class="offer">
    <h1 class="offer-title">Investment opportunities from £50,000 (€70,000)</h1>
    <p>Example: Suite Lorvette</p>
    <p>€70,000 long term loan to Château de Vormelle (estimated repayment after 20<br>years)</p>
    <p>Stay 4 weeks of your choice per year for the duration of your investment in Suite<br>Lorvette<br>Opportunity to rent unused weeks privately to friends and family.<br>(Rules apply)</p>
    <p>Shares in company owning property =&nbsp; 0.8%,<br>
      <span class="indent">ie: if the property is ever sold you receive 0.8% of proceeds</span>
      <span class="indent">Shares can be sold on the open market</span></p>
    <p>Shares in company renting out the accommodation = 1.67%<br>
      <span class="indent">ie: you get 1.67% of profits generated by the rental company.</span>
      <span class="indent">Forecast 2.95% pa yield or €1,917 pa&nbsp; after three years</span>
      <span class="indent">Accountant prepared forecasts available for review</span></p>
  </section>
</main>
</body>
</html>
```